Business Coach needs an elegant business card design

I need a business card design based around my logo for color and to look like a millionaire dollar coach. Incorporate the color of my logo with something creative and attractive that stands out. I am focused on high end companies and the card must look and feel that way.

Target Market(s)

High End Companies and Business Owners - Training People to become millionaires

Industry/Entity Type

Business

Requirements
Must have
• Front -
Logo (attached file) - Website (marlowkeeve.com) - Name (Marlow Keeve) Phone (555.201.7746) - Email (marlow@marlowkeeve.com) (My Title - Success Coach)
Back -
Slogan - Vision (see it) . Action (do it) . Transformation (be it)
Website - Learn More @ marlowkeeve.com

Creative High End Look!
Nice to have
Should not have
• Cheap standard look
nothing traditional

```html
<!DOCTYPE html>
<html lang="en">
<head>
<meta charset="utf-8">
<title>Marlow Keeve Coaching – Business Card</title>
<link rel="stylesheet" href="https://fonts.googleapis.com/css2?family=Open+Sans:wght@400;600;700&display=swap">
<style>
  :root {
    --navy: #1c2447;
    --ink: #2e2e33;
    --muted: #55585f;
    --page: #e9e9ea;
    --card-front: #ffffff;
    --card-back: #f1f1f0;
    --ghost: #e6e6e6;
    --ghost-back: #dcdcdb;
  }
  * { box-sizing: border-box; margin: 0; padding: 0; }
  html, body {
    width: 1200px; height: 675px; overflow: hidden;
    background: var(--page);
    font-family: "Open Sans", Arial, sans-serif;
  }
  .canvas { position: relative; width: 1200px; height: 675px; }
  .card {
    position: absolute; top: 189px;
    width: 520px; height: 297px;
    overflow: hidden;
    box-shadow: 0 4px 14px rgba(0,0,0,0.12);
  }
  .card--front { left: 60px; background: var(--card-front); }
  .card--back { left: 620px; background: var(--card-back); }

  .ghost-ring { position: absolute; }

  /* front */
  .brand {
    position: absolute; left: 28px; top: 40px;
    display: flex; align-items: center; gap: 12px;
  }
  .brand__dot {
    width: 48px; height: 48px; border-radius: 50%;
    background: var(--navy); flex: none;
  }
  .brand__name {
    display: block; width: 170px;
    font-size: 17px; font-weight: 600; letter-spacing: 2px;
    color: var(--navy); text-transform: uppercase; line-height: 1.25;
  }
  .contact {
    position: absolute; left: 268px; top: 96px; width: 240px;
  }
  .contact__rule { height: 1px; background: var(--navy); margin-bottom: 10px; }
  .contact__name { font-size: 15px; font-weight: 700; color: var(--navy); line-height: 1.2; }
  .contact__title { font-size: 10px; color: var(--muted); margin-bottom: 8px; }
  .contact__list { list-style: none; }
  .contact__item {
    display: flex; align-items: center; gap: 12px;
    font-size: 13px; color: var(--ink); line-height: 20px;
  }
  .contact__icon { width: 13px; height: 13px; fill: var(--navy); flex: none; }

  /* back */
  .slogan {
    position: absolute; left: 150px; top: 92px; width: 340px;
    color: var(--ink); font-size: 15px; line-height: 22px;
  }
  .slogan__line strong { color: var(--navy); font-weight: 700; text-transform: uppercase; }
  .slogan__line:nth-child(2) { padding-left: 22px; }
  .slogan__more { margin-top: 14px; padding-left: 40px; font-size: 12px; }
  .slogan__more strong { color: var(--navy); font-weight: 700; }
</style>
</head>
<body>
<main class="canvas">

  <section class="card card--front" aria-label="Card front">
    <svg class="ghost-ring" style="left:40px;top:100px" width="200" height="200" viewBox="0 0 200 200" aria-hidden="true">
      <circle cx="100" cy="100" r="90" fill="none" stroke="var(--ghost)" stroke-width="10"/>
    </svg>

    <div class="brand">
      <span class="brand__dot" aria-hidden="true"></span>
      <span class="brand__name">Marlow Keeve Coaching</span>
    </div>

    <div class="contact">
      <div class="contact__rule"></div>
      <p class="contact__name">Marlow Keeve</p>
      <p class="contact__title">Success Coach</p>
      <ul class="contact__list">
        <li class="contact__item">
          <svg class="contact__icon" viewBox="0 0 16 16" aria-hidden="true"><path d="M1 5c0-2 3-3 7-3s7 1 7 3v1h-3.5V4.5h-7V6H1zM3 7h10l1.5 7h-13zM8 9a2 2 0 1 0 0 4a2 2 0 0 0 0-4z"/></svg>
          555.201.7746
        </li>
        <li class="contact__item">
          <svg class="contact__icon" viewBox="0 0 16 16" aria-hidden="true"><path d="M1 3h14v10H1zM2.5 4.5l5.5 4.5 5.5-4.5v-.2h-11z"/></svg>
          marlow@marlowkeeve.com
        </li>
        <li class="contact__item">
          <svg class="contact__icon" viewBox="0 0 16 16" aria-hidden="true"><circle cx="8" cy="8" r="7"/><path d="M1 8h14M8 1c-3 3-3 11 0 14M8 1c3 3 3 11 0 14" stroke="#fff" stroke-width="1" fill="none"/></svg>
          www.marlowkeeve.com
        </li>
      </ul>
    </div>
  </section>

  <section class="card card--back" aria-label="Card back">
    <svg class="ghost-ring" style="left:60px;top:20px" width="260" height="260" viewBox="0 0 260 260" aria-hidden="true">
      <circle cx="130" cy="130" r="118" fill="none" stroke="var(--ghost-back)" stroke-width="12"/>
    </svg>

    <div class="slogan">
      <p class="slogan__line"><strong>Vision.</strong> See What You Want</p>
      <p class="slogan__line"><strong>Action.</strong> Do What It Takes</p>
      <p class="slogan__line"><strong>Transformation.</strong> Live Your Vision!</p>
      <p class="slogan__more"><strong>Learn More:</strong> www.marlowkeeve.com</p>
    </div>
  </section>

</main>
</body>
</html>
```